Elegant Black Candle Label Design!

I need a 2.375" tall by 3.0" wide candle label design. I'm looking for simple and elegant. Black label with silver leaf border and lettering. Label needs to have the following information on it: Fern Hollow Candle Co. as the company name, scent name in the middle and in smaller font, it needs to say Made in USA, All Natural, 8oz. Attached photos are for inspiration.

Target Market(s)

People looking for high end, all natural candle fragrances

Industry/Entity Type

Candle-Spa

Colors

Designer to choose only greyscale colors for use in the design.

Requirements
Must have
• Company Name, Scent (ability to change scent names), All Natural, Made in USA, 8oz
Nice to have
• Black background, silver leaf border and silver leaf font. Elegant fonts maybe slightly cursive

```html
<!DOCTYPE html>
<html lang="en">
<head>
<meta charset="utf-8">
<title>Fern Hollow Candle Co. – Label Versions</title>
<link href="https://fonts.googleapis.com/css2?family=Montserrat:wght@400;500;600;700&family=Ms+Madi&display=swap" rel="stylesheet">
<style>
  :root {
    --backdrop: #dedede;
    --backdrop-edge: #cfcfcf;
    --caption: #8c8c8c;
    --label-black: #0b0b0b;
    --label-black-soft: #161616;
    --silver-light: #f4f4f4;
    --silver-mid: #b9b9b9;
    --silver-dark: #6f6f6f;
    --ink: #ffffff;
  }
  * { box-sizing: border-box; margin: 0; padding: 0; }
  html, body {
    width: 1200px; height: 635px; overflow: hidden;
    background: radial-gradient(ellipse at center, var(--backdrop) 0%, var(--backdrop-edge) 100%);
    font-family: "Montserrat", sans-serif;
  }
  .sheet { display: flex; width: 1200px; height: 635px; }
  .version {
    position: relative; width: 600px; height: 635px;
    display: flex; flex-direction: column; align-items: center;
  }
  .version + .version { border-left: 1px solid #cacaca; }
  .version-caption {
    margin-top: 40px; height: 50px;
    font-weight: 700; font-size: 30px; letter-spacing: 0.12em;
    color: var(--caption);
  }
  .label {
    position: relative; width: 532px; height: 420px; margin-top: 20px;
    background: radial-gradient(ellipse at 50% 45%, var(--label-black-soft) 0%, var(--label-black) 75%);
    box-shadow: 0 6px 18px rgba(0,0,0,0.25);
    color: var(--ink);
  }
  .frame-outer, .frame-dots, .frame-inner { position: absolute; pointer-events: none; }
  .frame-outer { inset: 8px; border: 1.5px solid var(--silver-mid); }
  .frame-dots { inset: 15px; border: 2px dotted var(--silver-mid); }
  .frame-inner { inset: 24px; border: 1px solid var(--silver-dark); }
  .label-content {
    position: absolute; inset: 24px;
    display: flex; flex-direction: column; align-items: center;
  }
  .brand-caps {
    margin-top: 36px; font-weight: 700; font-size: 25px; letter-spacing: 0.16em;
  }
  .brand-sub {
    font-weight: 500; font-size: 17px; letter-spacing: 0.24em; margin-top: 2px;
  }
  .scent-script {
    margin-top: 34px; font-family: "Ms Madi", cursive; font-size: 88px; line-height: 1;
    background: linear-gradient(100deg, var(--silver-mid) 0%, var(--silver-light) 40%, var(--silver-dark) 70%, var(--silver-light) 100%);
    -webkit-background-clip: text; background-clip: text; color: transparent;
  }
  .brand-script {
    margin-top: 38px; font-family: "Ms Madi", cursive; font-size: 86px; line-height: 1; color: var(--ink);
  }
  .brand-script + .brand-sub { font-size: 20px; margin-top: 4px; }
  .scent-caps {
    margin-top: 28px; font-weight: 700; font-size: 28px; letter-spacing: 0.1em;
    background: linear-gradient(100deg, var(--silver-dark) 0%, var(--silver-light) 35%, var(--silver-mid) 65%, var(--silver-light) 100%);
    -webkit-background-clip: text; background-clip: text; color: transparent;
  }
  .claims {
    display: flex; width: 384px; height: 42px;
    border-top: 1.5px solid var(--silver-mid); border-bottom: 1.5px solid var(--silver-mid);
  }
  .version--one .claims { margin-top: 40px; }
  .version--two .claims { margin-top: 16px; }
  .claim {
    flex: 1; display: flex; align-items: center; justify-content: center;
    font-size: 11.5px; font-weight: 500; letter-spacing: 0.32em;
  }
  .claim + .claim { border-left: 1.5px solid var(--silver-mid); }
  .net-weight {
    margin-top: 12px; display: flex; align-items: center; gap: 8px;
    font-weight: 500; font-size: 20px;
  }
  .net-weight svg { display: block; }
</style>
</head>
<body>
<main class="sheet">

  <section class="version version--one">
    <h2 class="version-caption">VERSION 1</h2>
    <article class="label">
      <div class="frame-outer"></div>
      <div class="frame-dots"></div>
      <div class="frame-inner"></div>
      <div class="label-content">
        <p class="brand-caps">FERN HOLLOW</p>
        <p class="brand-sub">CANDLE CO.</p>
        <p class="scent-script">Scent name</p>
        <div class="claims">
          <span class="claim">ALL NATURAL</span>
          <span class="claim">MADE IN USA</span>
        </div>
        <p class="net-weight">
          <svg width="22" height="6" viewBox="0 0 22 6"><circle cx="3" cy="3" r="1.6" fill="#fff"/><circle cx="10" cy="3" r="1.8" fill="#fff"/><circle cx="18" cy="3" r="2.6" fill="#fff"/></svg>
          8oz
          <svg width="22" height="6" viewBox="0 0 22 6"><circle cx="4" cy="3" r="2.6" fill="#fff"/><circle cx="12" cy="3" r="1.8" fill="#fff"/><circle cx="19" cy="3" r="1.6" fill="#fff"/></svg>
        </p>
      </div>
    </article>
  </section>

  <section class="version version--two">
    <h2 class="version-caption">VERSION 2</h2>
    <article class="label">
      <div class="frame-outer"></div>
      <div class="frame-dots"></div>
      <div class="frame-inner"></div>
      <div class="label-content">
        <p class="brand-script">Fern Hollow</p>
        <p class="brand-sub">CANDLE CO.</p>
        <p class="scent-caps">SCENT NAME</p>
        <div class="claims">
          <span class="claim">ALL NATURAL</span>
          <span class="claim">MADE IN USA</span>
        </div>
        <p class="net-weight">
          <svg width="22" height="6" viewBox="0 0 22 6"><circle cx="3" cy="3" r="1.6" fill="#fff"/><circle cx="10" cy="3" r="1.8" fill="#fff"/><circle cx="18" cy="3" r="2.6" fill="#fff"/></svg>
          8oz
          <svg width="22" height="6" viewBox="0 0 22 6"><circle cx="4" cy="3" r="2.6" fill="#fff"/><circle cx="12" cy="3" r="1.8" fill="#fff"/><circle cx="19" cy="3" r="1.6" fill="#fff"/></svg>
        </p>
      </div>
    </article>
  </section>

</main>
</body>
</html>
```